Fontenot Bayou Grillhouse (Owners Card)

Need a classy, but modern business card. I have included a promotional card for the steakhouse. I need one for myself (the owner) that is more professional.

Target Market(s)

General Public

Industry/Entity Type

Food service

Contact Information for Business Card

Name, business address, phone number, email, logo

Font styles to use
Serif
Sans Serif
Decorative
Script

Requirements
Must have
• My name (Darvel Pruitt), business address (327 Oakmere Street), phone number (510) 493-2615, email (Dpruittkr4@mailvane.example. On the back of the card: Psalms 27 1 The LORD is my light and my salvation— whom shall I fear? The LORD is the stronghold of my life— of whom shall I be afraid? 2 When the wicked advance against me to devour me, it is my enemies and my foes who will stumble and fall. 3 Though an army besiege me, my heart will not fear; though war break out against me, even then I will be confident.
Nice to have
• Something that’s bold, but modern and professional.

```html
<!DOCTYPE html>
<html lang="en">
<head>
<meta charset="utf-8">
<title>Fontenot Bayou Grillhouse — Owner Business Card</title>
<link rel="stylesheet" href="https://fonts.googleapis.com/css2?family=Open+Sans:wght@400;700&display=swap">
<style>
  :root {
    --page: #ffffff;
    --card: #000000;
    --ink: #ffffff;
    --brand: #f2b21c;
    --brand-dot: #e8432b;
  }
  * { box-sizing: border-box; margin: 0; padding: 0; }
  html, body {
    width: 1200px; height: 450px; overflow: hidden;
    background: var(--page);
    font-family: "Open Sans", sans-serif;
  }
  .sheet { position: relative; width: 1200px; height: 450px; }
  .card {
    position: absolute; top: 75px;
    width: 527px; height: 301px;
    background: var(--card); color: var(--ink);
  }
  .card--front { left: 51px; }
  .card--back { left: 625px; }

  /* Front */
  .brand {
    position: absolute; left: 60px; top: 152px;
    width: 150px; height: 150px;
    display: flex; flex-direction: column; align-items: center; justify-content: center;
    gap: 10px; text-align: center;
  }
  .brand__dot {
    width: 34px; height: 34px; border-radius: 50%;
    background: var(--brand-dot);
  }
  .brand__name {
    color: var(--brand); font-weight: 700;
    font-size: 17px; line-height: 1.15; letter-spacing: 0.02em;
  }
  .divider {
    position: absolute; left: 263px; top: 78px;
    width: 2px; height: 152px; background: var(--ink);
  }
  .contact {
    position: absolute; left: 270px; top: 92px; width: 236px;
    text-align: center;
  }
  .contact__name { font-size: 19px; font-weight: 400; letter-spacing: 0.01em; margin-bottom: 16px; }
  .contact__line { font-size: 15.5px; line-height: 23px; }

  /* Back */
  .rule {
    position: absolute; left: 22px; width: 483px; height: 1.5px; background: var(--ink);
  }
  .rule--top { top: 18px; }
  .rule--bottom { top: 283px; }
  .verse {
    position: absolute; left: 54px; top: 90px; width: 418px;
    font-size: 14.4px; line-height: 18.7px; text-align: justify;
  }
</style>
</head>
<body>
<main class="sheet">
  <section class="card card--front" aria-label="Card front">
    <div class="brand">
      <span class="brand__dot" aria-hidden="true"></span>
      <span class="brand__name">FONTENOT BAYOU GRILLHOUSE</span>
    </div>
    <div class="divider" aria-hidden="true"></div>
    <div class="contact">
      <h1 class="contact__name">DARVEL PRUITT</h1>
      <p class="contact__line">327 Oakmere Street</p>
      <p class="contact__line">(510) 493-2615</p>
      <p class="contact__line">Dpruittkr4@mailvane.example</p>
    </div>
  </section>

  <section class="card card--back" aria-label="Card back">
    <div class="rule rule--top" aria-hidden="true"></div>
    <p class="verse">Psalms 27 1 The LORD is my light and my salvation– whom shall I fear? The LORD is the stronghold of my life – of whom shall I be afraid? 2 When the wicked advance against me to devour me, it is my enemies and my foes who will stumble and fall. 3 Though an army besiege me, my heart will not fear; though war break out against me, even then I will be confident.</p>
    <div class="rule rule--bottom" aria-hidden="true"></div>
  </section>
</main>
</body>
</html>
```